New Medical Practice Flyer/Announcement

Need a postcard size flyer for a new medical practice opening up. Need the medical provider's name and credentials, the office phone number, address and website on the inside. It is a unique holistic medical practice with a focus on kidney disease and eating disorders in addition to preventative health and diabetes/hypertension management. The look and design should be calming and natural with elements of elegance and sophistication.

Target Market(s)

Patients

Industry/Entity Type

Healthcare

Requirements
Must have
• Change to postcard format for direct mailing. Need logo in large print on front and back with address and Introduction.
Nice to have
• - The front of the postcard should have the logo in big print.
• - Back of postcard should have the script " Introducing a unique and customized medical practice to your health needs."
• - Dr. Marta Quillon, with credentials
• - Phone number and website
• - Email
• - Image of bubbles on the back of the card.

```html
<!DOCTYPE html>
<html lang="en">
<head>
<meta charset="utf-8">
<title>Marta J. Quillon, DO – Practice Announcement Postcard</title>
<link rel="stylesheet" href="https://fonts.googleapis.com/css2?family=Lato:wght@300;400;700;900&family=Arimo:wght@400;700&display=swap">
<style>
  :root {
    --paper: #ffffff;
    --ink: #352b57;
    --ink-soft: #3d3550;
    --icon: #8fb0aa;
    --tone-blue: #b4c2dc;
    --tone-green: #cde3c0;
    --tone-mint: #e3efe8;
    --tone-lavender: #dcd7ea;
    --postal: #111111;
  }
  * { margin: 0; padding: 0; box-sizing: border-box; }
  html, body { width: 1200px; height: 871px; overflow: hidden; background: var(--paper); }
  .postcard { position: relative; width: 1200px; height: 871px; background: var(--paper); font-family: "Lato", sans-serif; color: var(--ink); }
  .bubble-field {
    position: absolute; left: 97px; top: 53px; width: 633px; height: 209px;
    border-radius: 105px;
    background: linear-gradient(100deg, var(--tone-blue) 0%, var(--tone-mint) 28%, var(--tone-green) 52%, var(--tone-blue) 72%, var(--tone-lavender) 100%);
    opacity: 0.55;
  }
  .headline { position: absolute; left: 127px; top: 286px; width: 700px; font-weight: 300; font-size: 51px; line-height: 62px; letter-spacing: -0.3px; color: var(--ink); }
  .provider { position: absolute; left: 128px; top: 512px; }
  .provider-name { font-weight: 900; font-size: 34px; line-height: 44px; letter-spacing: -0.6px; color: var(--ink); }
  .provider-credentials { font-size: 22px; line-height: 27px; color: var(--ink-soft); }
  .contact-list { position: absolute; left: 127px; top: 628px; list-style: none; }
  .contact-item { display: flex; align-items: center; height: 36px; font-size: 24px; color: var(--ink-soft); }
  .contact-item:nth-child(4) { margin-top: 3px; }
  .contact-icon { width: 28px; height: 30px; margin-right: 11px; flex: none; }
  .postal-indicia { position: absolute; left: 1051px; top: 46px; width: 96px; height: 95px; border: 2px solid var(--postal); font-family: "Arimo", sans-serif; font-size: 10.5px; line-height: 13.2px; text-align: center; color: var(--postal); padding-top: 10px; }
  .postal-indicia strong { font-weight: 700; }
  .postal-address { position: absolute; left: 892px; top: 149px; width: 255px; height: 74px; border: 2px solid var(--postal); font-family: "Arimo", sans-serif; font-size: 14px; line-height: 17.5px; color: var(--postal); padding: 12px 0 0 8px; }
  .postal-route { padding-left: 5px; letter-spacing: 0.2px; }
</style>
</head>
<body>
<main class="postcard">
  <div class="bubble-field" role="img" aria-label="Decorative scattered bubbles in soft blue, green and lavender"></div>

  <h1 class="headline">Introducing a unique and customized medical practice to your health needs.</h1>

  <section class="provider">
    <h2 class="provider-name">Marta J. Quillon, DO</h2>
    <p class="provider-credentials">Nephrologist and Eating Disorder Specialist</p>
    <p class="provider-credentials">Board Certified, Nephrology and Internal Medicine</p>
  </section>

  <ul class="contact-list">
    <li class="contact-item">
      <svg class="contact-icon" viewBox="0 0 28 30" aria-hidden="true">
        <path d="M6 3 h4 l1.5 7 -3 2 c1 3.5 2.5 5.5 4.5 6.5 l2 -2.5 6 2.5 v4 c-1 3 -4 4.5 -7 3.5 C7 24 2.5 16 2.5 8.5 c0 -3 1.5 -5 3.5 -5.5z" fill="var(--icon)"/>
        <path d="M18 9 q2 2 0 4 M21 7 q4 4 0 8 M24 5 q6 6 0 12" fill="none" stroke="var(--icon)" stroke-width="1.6" stroke-linecap="round"/>
      </svg>
      <span>555.214.7390</span>
    </li>
    <li class="contact-item">
      <svg class="contact-icon" viewBox="0 0 28 30" aria-hidden="true">
        <circle cx="14" cy="15" r="5" fill="none" stroke="var(--icon)" stroke-width="3"/>
        <path d="M19 10 v7 c0 3 4 3 5 0 c2 -7 -3 -13 -10 -13 c-6 0 -11 5 -11 11 c0 7 6 12 14 10" fill="none" stroke="var(--icon)" stroke-width="3" stroke-linecap="round"/>
      </svg>
      <span>hello@quillonkidney.com</span>
    </li>
    <li class="contact-item">
      <svg class="contact-icon" viewBox="0 0 28 30" aria-hidden="true">
        <circle cx="13" cy="16" r="11" fill="none" stroke="var(--icon)" stroke-width="2"/>
        <path d="M2 16 h22 M13 5 v22 M5 9 h16 M5 23 h16" stroke="var(--icon)" stroke-width="2" fill="none"/>
        <ellipse cx="13" cy="16" rx="5" ry="11" fill="none" stroke="var(--icon)" stroke-width="2"/>
        <path d="M22 2 c-3 0 -4 2 -4 4 c0 2 4 6 4 6 s4 -4 4 -6 c0 -2 -1 -4 -4 -4z" fill="var(--icon)"/>
      </svg>
      <span>www.wholebodyrenal.com</span>
    </li>
    <li class="contact-item">
      <svg class="contact-icon" viewBox="0 0 28 30" aria-hidden="true">
        <path d="M14 1 c-7 0 -12 5 -12 11 c0 8 12 17 12 17 s12 -9 12 -17 c0 -6 -5 -11 -12 -11z" fill="var(--icon)"/>
        <circle cx="14" cy="12" r="4.5" fill="none" stroke="var(--paper)" stroke-width="2"/>
      </svg>
      <span>2140 Willowmere Ave, Suite 3</span>
    </li>
  </ul>

  <div class="postal-indicia">
    PRSRT STD<br>ECRWSS<br>U.S. POSTAGE<br><strong>PAID</strong><br>EDDM RETAIL
  </div>
  <div class="postal-address">
    <div class="postal-route">*******************ECRWSS****</div>
    <div>Local</div>
    <div>Postal Customer</div>
  </div>
</main>
</body>
</html>
```